VELT needs a simple, contemporary and easy to use 'designer' website (fully working/coded)

VELT is a progressive market research consultancy based in Sydney, Australia. We are a new company and require a contemporary/modern and bold, uncomplicated/simple, clean/uncluttered site, which uses friendly and easy to read fonts. The brand is approachable. The colour palate should be simple and contemporary. Colours used in our logo are:#FFCC00 and #404041 so any others should complement these.

The following website gives a really good idea of how simple the site should be: www.brightmarrow.com.au and I am looking to create something similar to this style of site (but not necessarily copied).

The website should convey ‘different types of customer’. VELT helps different companies ‘connect’ with their particular shoppers or end users of their product. This could be a mum doing the washing, a dad cleaning the car, children eating ice cream, old people reading the newspaper, someone trying on glasses, someone buying petfood etc. Alternatively it could simply just be pictures of different people…different ages, different nationalities, different employment types etc, but they should give a positive impression (ie people smiling/laughing) and also GREAT quality photos.

Content will also be attached but please note this is just a draft reference and will be sent to a copywriter for improvement. The telephone number is yet to be confirmed but will be given at the end of the contest.

The navigation may borrow strongly from www.brightmarrow.com.au. It may have the following navigation panel:

ABOUT US

WHAT WE DO

> NPD

> PRODUCT TESTING

> SHOPPER

> SEGMENTATION

> ONLINE COMMUNITIES

> CUSTOMER EXPERIENCE

> VISUALISATION

> TAILOR MADE

CONTACT US

The home page may be WHAT WE DO and each picture represents one of the 8 sections (such as NPD) etc.

One of my main objectives is also to get people to sign up to my quarterly newsletter, so would like to make this very visible, and make it easy for them to connect via workmesh.

I will also want to add a blog page in September (so needs to be hidden now but switched on in Sept). This blog will contain articles from the newsletters and workmesh updates. I may also want to add a simple 90-180 second video at the bottom of each of the 8 sections (to be added over the next 12 months but i would like to ensure it is possible to do this at a later stage).

The logo has recently been designed and i have attcahed different colour versions as i may be swayed depending on hoe they look in te website. I tend to prefer yellow on white, or white on yellow but other optins are included if you think they work better with your design.

Target Market(s)

Professionals in large blue chip companies..such as pino fizz, varona, tamborix etc. Marketing Managers/Directors, PR and advertising agencies etc.

Industry/Entity Type

Progressive

Requirements
Must have
• High quality positive photos. Be very easy to navigate...should scream simple!

```html
<!DOCTYPE html>
<html lang="en">
<head>
<meta charset="utf-8">
<title>VELT — What We Do</title>
<link rel="stylesheet" href="https://fonts.googleapis.com/css2?family=Ubuntu:wght@300;400;500;700&display=swap">
<style>
  :root {
    --brand-yellow: #ffcc00;
    --tile-yellow: #ffd52e;
    --ink: #404041;
    --rule: #d9d9d9;
    --chip: #e4e4e4;
    --footer: #000000;
    --white: #ffffff;
  }
  * { box-sizing: border-box; margin: 0; padding: 0; }
  html, body { width: 1200px; height: 955px; overflow: hidden; }
  body {
    position: relative;
    background: var(--white);
    font-family: "Ubuntu", "Helvetica Neue", Arial, sans-serif;
    color: var(--ink);
  }
  .top-band { position: absolute; left: 0; top: 0; width: 1200px; height: 6px; background: var(--brand-yellow); }

  .brand { position: absolute; left: 71px; top: 50px; width: 240px; }
  .brand-name {
    font-size: 76px; font-weight: 500; line-height: 1; letter-spacing: 1px;
    color: var(--brand-yellow);
  }
  .brand-tagline { margin: 4px 0 0 18px; font-size: 14px; font-weight: 400; color: var(--ink); }

  .site-nav { position: absolute; left: 63px; top: 220px; width: 241px; list-style: none; }
  .nav-main {
    display: flex; align-items: center; gap: 8px;
    height: 26px; font-size: 16px; font-weight: 500; color: var(--ink); text-transform: uppercase;
  }
  .nav-chip {
    width: 24px; height: 24px; border-radius: 50%; background: var(--chip);
    display: flex; align-items: center; justify-content: center;
  }
  .nav-rule { height: 1px; background: var(--rule); margin: 10px 0 10px 32px; }
  .nav-rule.after-sub { margin-top: 0; }
  .nav-sub { list-style: none; margin: 11px 0 0 35px; }
  .nav-sub li {
    display: flex; align-items: center; gap: 8px;
    height: 46px; font-size: 14px; font-weight: 300; color: var(--ink); text-transform: uppercase;
  }

  .tiles { position: absolute; left: 347px; top: 99px; width: 785px; height: 629px; }
  .tile { position: absolute; width: 261px; height: 207px; }
  .c1 { left: 0; } .c2 { left: 262px; } .c3 { left: 524px; }
  .r1 { top: 0; } .r2 { top: 208px; } .r3 { top: 416px; }

  .tile-feature {
    background: var(--tile-yellow);
    display: flex; flex-direction: column; align-items: center; justify-content: center; text-align: center;
  }
  .tile-feature h1 { font-size: 35px; font-weight: 700; color: #111; line-height: 1.1; }
  .tile-feature p { margin-top: 8px; font-size: 15px; font-weight: 300; line-height: 1.45; color: var(--ink); }

  .tile-newsletter {
    height: 213px; background: var(--brand-yellow); color: var(--white);
    display: flex; flex-direction: column; align-items: center; text-align: center; padding-top: 50px;
  }
  .tile-newsletter h2 { font-size: 23px; font-weight: 500; }
  .tile-newsletter p { margin-top: 4px; font-size: 13.5px; font-weight: 400; line-height: 1.35; }
  .btn-signup {
    margin-top: 16px; display: inline-flex; align-items: center; gap: 6px;
    height: 27px; padding: 0 12px; background: #000; border-radius: 2px;
    font-size: 14px; font-weight: 500; color: var(--brand-yellow); text-decoration: none;
  }

  .photo-clinical { background: linear-gradient(135deg, #dfe7f2, #b9c8dc 60%, #8aa6cc); }
  .photo-aisle { background: linear-gradient(120deg, #7a5a3a, #c9a777 45%, #dfe3ea 70%, #5e4a3c); }
  .photo-puzzle { background: radial-gradient(circle at 50% 60%, #f4f0ec, #e7cfc3 55%, #d9a897); }
  .photo-crowd { background: linear-gradient(160deg, #6b4a3a, #b07a5e 40%, #4f6b8d 70%, #8d3a3a); }
  .photo-handshake { background: linear-gradient(135deg, #eef1f3, #c9d2d8 45%, #27324a 80%); }
  .photo-building { background: linear-gradient(180deg, #3d7fc4, #9bc4e8 55%, #e9eef4); }
  .photo-tailor { background: linear-gradient(135deg, #4a3a36, #c98a5a 45%, #e39a2c 65%, #b01c24); }

  .site-footer {
    position: absolute; left: 0; top: 852px; width: 1200px; height: 103px; background: var(--footer);
    display: flex; align-items: center; justify-content: space-between; padding: 0 126px 0 75px;
    color: var(--white); font-size: 12.5px;
  }
  .social { display: flex; gap: 14px; list-style: none; font-size: 12.5px; font-weight: 500; }
</style>
</head>
<body>
  <div class="top-band"></div>

  <header class="brand">
    <div class="brand-name">VELT</div>
    <div class="brand-tagline">progressive research</div>
  </header>

  <nav>
    <ul class="site-nav">
      <li class="nav-main">
        <span class="nav-chip"><svg width="8" height="10" viewBox="0 0 8 10"><path d="M2 1l4 4-4 4" fill="none" stroke="#404041" stroke-width="1.8"/></svg></span>ABOUT US
      </li>
      <li class="nav-rule"></li>
      <li class="nav-main">
        <span class="nav-chip"><svg width="8" height="10" viewBox="0 0 8 10"><path d="M2 1l4 4-4 4" fill="none" stroke="#404041" stroke-width="1.8"/></svg></span>WHAT WE DO
      </li>
      <li>
        <ul class="nav-sub">
          <li><svg width="7" height="12" viewBox="0 0 7 12"><path d="M1 1l5 5-5 5" fill="none" stroke="#ffcc00" stroke-width="2"/></svg>NPD</li>
          <li><svg width="7" height="12" viewBox="0 0 7 12"><path d="M1 1l5 5-5 5" fill="none" stroke="#ffcc00" stroke-width="2"/></svg>Product Testing</li>
          <li><svg width="7" height="12" viewBox="0 0 7 12"><path d="M1 1l5 5-5 5" fill="none" stroke="#ffcc00" stroke-width="2"/></svg>Shopper</li>
          <li><svg width="7" height="12" viewBox="0 0 7 12"><path d="M1 1l5 5-5 5" fill="none" stroke="#ffcc00" stroke-width="2"/></svg>Segmentation</li>
          <li><svg width="7" height="12" viewBox="0 0 7 12"><path d="M1 1l5 5-5 5" fill="none" stroke="#ffcc00" stroke-width="2"/></svg>Online Communities</li>
          <li><svg width="7" height="12" viewBox="0 0 7 12"><path d="M1 1l5 5-5 5" fill="none" stroke="#ffcc00" stroke-width="2"/></svg>Customer Experience</li>
          <li><svg width="7" height="12" viewBox="0 0 7 12"><path d="M1 1l5 5-5 5" fill="none" stroke="#ffcc00" stroke-width="2"/></svg>Visualisation</li>
          <li><svg width="7" height="12" viewBox="0 0 7 12"><path d="M1 1l5 5-5 5" fill="none" stroke="#ffcc00" stroke-width="2"/></svg>Tailor Made</li>
        </ul>
      </li>
      <li class="nav-rule after-sub"></li>
      <li class="nav-main">
        <span class="nav-chip"><svg width="8" height="10" viewBox="0 0 8 10"><path d="M2 1l4 4-4 4" fill="none" stroke="#404041" stroke-width="1.8"/></svg></span>CONTACT US
      </li>
    </ul>
  </nav>

  <main class="tiles">
    <section class="tile tile-feature c1 r1">
      <h1>NPD</h1>
      <p>Maecenas aliquet velit vel<br>auris neque metus</p>
    </section>
    <div class="tile photo-clinical c2 r1" role="img" aria-label="Two lab technicians in hairnets and masks reviewing a product jar"></div>
    <div class="tile photo-aisle c3 r1" role="img" aria-label="Shopper reading a product label in a store aisle"></div>
    <div class="tile photo-puzzle c1 r2" role="img" aria-label="Hands joining two white puzzle pieces"></div>
    <div class="tile photo-crowd c2 r2" role="img" aria-label="Large group of smiling people of different ages and backgrounds"></div>
    <div class="tile photo-handshake c3 r2" role="img" aria-label="Business people shaking hands across a desk"></div>
    <div class="tile photo-building c1 r3" role="img" aria-label="Modern building blending into an architectural wireframe"></div>
    <div class="tile photo-tailor c2 r3" role="img" aria-label="Woman fitting a red garment on a dress form"></div>
    <section class="tile tile-newsletter c3 r3">
      <h2>Newsletter Sign Up</h2>
      <p>Please sign up here for latest<br>news &amp; offers</p>
      <a class="btn-signup" href="#">Click here <svg width="5" height="8" viewBox="0 0 5 8"><path d="M0 0l5 4-5 4z" fill="#ffcc00"/></svg></a>
    </section>
  </main>

  <footer class="site-footer">
    <p>Copyright © 2013 Company Name.&nbsp; All right reserved.&nbsp; Term of Use</p>
    <ul class="social">
      <li>friendloop</li>
      <li>workmesh</li>
      <li>chirpline</li>
    </ul>
  </footer>
</body>
</html>
```